Diesel Trailer Manufacturer Website Design

We are working with a Trailer Manufacturer in Texas. They provide custom-made trailers for diesel trucks throughout the US.
Some sites to use for content/competitors:
www.quillontrailer.com
https://velmortrailers.com
http://www.dunsworthcustomtrailers.com/
https://www.pelhamtrailer.com
https://www.haulzenith.com
Thank you for taking the time to consider designing a website for us. We are web developers based in Stockton, CA, USA. Most of our projects go through the same process. Understanding this process may help you win a project with us. We custom-code all of our websites in-house. We don’t have any requirements as to what tools you use for your design, but we ask that you follow these guidelines.
IMAGES:
If you use any images or icons in the design, we ask that you have a link to the asset so we can purchase the image/icon. Most of the designs we submit do not have the customer’s images on them unless they have some great images. Be creative; show us the feeling you are trying to portray with your image choices. Use any royalty-free site you choose. We subscribe to Vornix and mainly use their images, but we can purchase images outside of Vornix. PLEASE NOTE: we will not submit designs to clients with watermarks on the images.
FONTS:
We ask that you identify the fonts you’re using in the design. This can be done in a message if you want. We typically use Tellura Fonts and Vornix Fonts.
CONTENT:
We're always open to different content and ideas. We often submit designs with stock images so the client can see our vision. We typically take pictures after the website launch to use their images with our vision. Lorem Ipsum is fine for paragraphs, but we ask that you make the Headers with correct English. We want to be able to show the vision and identify the sections of the website.
INSPIRATION:
We typically add a couple of links in the brief of websites we like to help you get started in your design.
REVISIONS:
We do not often ask for revisions of the designs unless we see something in the design that may not appeal to the client. If there are slight changes that we want to make, we do that in the development process.
FEEDBACK:
We rarely give feedback on designs during the design process. We are working on many website projects and do not have the time to provide feedback. We usually respond if your request is well thought out and asks specific questions, but a note asking “feedback, please” usually goes unanswered.

```html
<!DOCTYPE html>
<html lang="en">
<head>
<meta charset="utf-8">
<title>Calderwood — Texas Trailers</title>
<link href="https://fonts.googleapis.com/css2?family=Poppins:wght@400;500;600;700&display=swap" rel="stylesheet">
<style>
:root{
  --blue:#3d97c0;
  --blue-dark:#2f6f95;
  --ink:#111418;
  --muted:#3a3f47;
  --link:#2a5f86;
  --soft:#f4f6f8;
  --stats:#e8e8e8;
  --footer:#23252a;
  --white:#ffffff;
}
*{margin:0;padding:0;box-sizing:border-box}
html,body{width:1200px;height:2957px;overflow:hidden}
body{font-family:'Poppins',sans-serif;color:var(--ink);background:var(--white);position:relative}
.abs{position:absolute}

/* hero */
.hero{left:0;top:0;width:1200px;height:734px;overflow:hidden}
.hero-photo{position:absolute;inset:0;background:linear-gradient(180deg,#b9c3c8 0%,#8f9698 30%,#7d6a55 60%,#5a4735 100%)}
.hero-overlay{position:absolute;inset:0}
.brand-mark{left:75px;top:46px;display:flex;align-items:center;gap:6px;color:var(--white);font-size:13px;font-weight:600}
.brand-dot{width:11px;height:11px;border-radius:50%;background:var(--white)}
.nav{left:238px;top:48px;display:flex;gap:34px;font-size:13px;color:var(--white)}
.hero-title{left:67px;top:200px;width:960px;font-size:49px;font-weight:600;line-height:70px;color:var(--white)}
.hero-rule{left:66px;top:426px;width:469px;height:3px;background:var(--white)}
.hero-text{left:67px;top:450px;width:920px;font-size:13.5px;line-height:20px;color:var(--white)}
.btn-outline{display:flex;align-items:center;justify-content:center;border:1.5px solid var(--white);border-radius:24px;color:var(--white);font-size:13px;font-weight:600}
.hero-btn{left:67px;top:556px;width:133px;height:44px}

/* feature cards */
.card{top:696px;width:333px;height:216px;background:var(--white);border-radius:16px;box-shadow:0 4px 14px rgba(0,0,0,.12);padding:62px 16px 0 17px}
.card h3{font-size:18px;font-weight:500;margin-bottom:8px}
.card p{font-size:12.5px;line-height:17.5px;color:var(--muted)}
.card a{display:block;margin-top:6px;font-size:12px;color:var(--link);text-decoration:none}
.card-icon{position:absolute;left:50%;top:-42px;margin-left:-40px;width:80px;height:80px;border-radius:50%;background:var(--white);border:3px solid #d8e8f0;display:flex;align-items:center;justify-content:center}

/* about */
.about{left:0;top:1046px;width:1200px;height:591px;background:linear-gradient(100deg,var(--soft) 72%,#9cc9dd 88%,#5fa9cb 100%)}
.eyebrow{left:117px;top:1113px;font-size:27px;font-weight:500}
.about-title{left:117px;top:1180px;width:980px;font-size:40px;font-weight:600;line-height:60px}
.about-text{left:117px;top:1440px;width:960px;font-size:13.5px;line-height:20px;color:var(--ink)}
.btn-fill{display:flex;align-items:center;justify-content:center;background:var(--blue);border-radius:24px;color:var(--white);font-size:13px;font-weight:600}
.about-btn{left:117px;top:1526px;width:133px;height:44px}

/* gallery */
.gallery-title{left:0;top:1704px;width:1200px;text-align:center;font-size:27px;font-weight:500}
.g-item{width:277px;height:150px}
.g-label{position:absolute;left:33px;top:0;font-size:17px;font-weight:500;color:var(--blue-dark)}
.g-arrow{position:absolute;right:33px;top:-2px}
.g-photo{position:absolute;left:0;top:92px;width:277px;height:48px;border-radius:10px}
.see-all{left:533px;top:2157px;width:133px;height:44px}

/* stats */
.stats{left:0;top:2267px;width:1200px;height:236px;background:var(--stats)}
.stat{width:260px;text-align:center}
.stat b{display:block;font-size:34px;font-weight:600;line-height:40px}
.stat span{display:block;margin-top:12px;font-size:17.5px;font-weight:500;color:var(--blue-dark)}

/* contact band */
.touch{left:0;top:2503px;width:1200px;height:117px;background:var(--blue)}
.touch h2{position:absolute;left:117px;top:40px;font-size:34px;font-weight:600;color:var(--white);line-height:40px}
.touch-btn{left:877px;top:41px;width:206px;height:44px}

/* footer */
.footer{left:0;top:2620px;width:1200px;height:337px;background:var(--footer);color:var(--white)}
.footer h4{font-size:17px;font-weight:600}
.f-brand{left:105px;top:38px}
.f-about{left:105px;top:78px;width:380px;font-size:13.5px;line-height:20px}
.f-news{left:105px;top:158px}
.f-input{left:105px;top:195px;width:332px;height:39px;border-radius:20px;background:var(--white);color:#8a8f96;font-size:10px;padding:13px 20px}
.f-go{left:446px;top:195px;width:50px;height:39px;border-radius:20px;background:var(--blue);display:flex;align-items:center;justify-content:center;font-size:15px;font-weight:600}
.f-col{top:36px}
.f-col ul{list-style:none;margin-top:14px;font-size:13.5px}
.f-col li{height:40px}
.socials{display:flex;gap:20px;margin-top:18px}
.socials span{width:20px;height:20px;border-radius:50%;background:var(--white);display:block}
.copyright{left:119px;top:294px;font-size:13.5px}
</style>
</head>
<body>

<section class="hero abs">
  <div class="hero-photo" role="img" aria-label="Construction site with a dump truck, excavator and earthworks"></div>
  <svg class="hero-overlay" width="1200" height="734" viewBox="0 0 1200 734" aria-hidden="true">
    <polygon points="0,0 172,0 766,734 0,734" fill="#3d97c0" fill-opacity=".82"/>
  </svg>
  <div class="brand-mark abs"><span class="brand-dot"></span>Calderwood</div>
  <nav class="nav abs"><span>HOME</span><span>ABOUT US</span><span>GALLERY</span><span>CONTACT</span></nav>
  <h1 class="hero-title abs">Texas Trailers: Crafting Customized Excellence for Diesel Trucks Across the USA!</h1>
  <div class="hero-rule abs"></div>
  <p class="hero-text abs">Lorem ipsum dolor sit amet consectetur. Egestas non viverra adipiscing in varius tortor. Mauris varius nunc enim bibendum habitasse convallis interdum. Faucibus risus mauris vestibulum quisque purus pharetra. Elit at eu diam placerat molestie blandit consectetur. Condimentum accumsan hac enim sit urna eu dolor neque aenean. Dignissim cras massa nibh purus consequat est. Morbi at nisl lacus sem.</p>
  <div class="btn-outline hero-btn abs">READ MORE</div>
</section>

<article class="card abs" style="left:67px">
  <div class="card-icon"><svg width="34" height="34" viewBox="0 0 34 34"><circle cx="17" cy="17" r="11" fill="none" stroke="#3d97c0" stroke-width="3" stroke-dasharray="4 2.5"/><circle cx="17" cy="17" r="4" fill="#3d97c0"/></svg></div>
  <h3>Precision Engineering</h3>
  <p>Meticulous craftsmanship to ensure every trailer meets the highest standards of quality and durability.</p>
  <a>Read More &gt;</a>
</article>
<article class="card abs" style="left:434px">
  <div class="card-icon"><svg width="34" height="34" viewBox="0 0 34 34"><circle cx="17" cy="13" r="8" fill="#3d97c0"/><rect x="13" y="22" width="8" height="7" rx="2" fill="#2f6f95"/></svg></div>
  <h3>Tailored Solutions</h3>
  <p>Customized trailer designs to perfectly match the unique specifications and preferences of each diesel truck owner.</p>
  <a>Read More &gt;</a>
</article>
<article class="card abs" style="left:800px">
  <div class="card-icon"><svg width="34" height="34" viewBox="0 0 34 34"><circle cx="17" cy="13" r="9" fill="none" stroke="#3d97c0" stroke-width="2.5"/><path d="M8 13h18M17 4v18" stroke="#3d97c0" stroke-width="2"/><path d="M5 27q12 6 24-2" fill="none" stroke="#2f6f95" stroke-width="3"/></svg></div>
  <h3>Nationwide Delivery</h3>
  <p>Seamless logistics for hassle-free delivery anywhere in the United States, bringing exceptional trailers right to your doorstep.</p>
  <a>Read More &gt;</a>
</article>

<section class="about abs"></section>
<div class="eyebrow abs">About Us</div>
<svg class="abs" style="left:116px;top:1153px" width="140" height="12" viewBox="0 0 140 12" aria-hidden="true"><path d="M0 6h136M130 1l6 5-6 5" fill="none" stroke="#111418" stroke-width="1.6"/></svg>
<h2 class="about-title abs">Unleashing Innovation on Wheels: Discover the Story Behind Texas Trailers, Your Trusted Partner in Crafting Tailored Solutions for Diesel Truck Enthusiasts Nationwide!</h2>
<p class="about-text abs">Lorem ipsum dolor sit amet consectetur. Egestas non viverra adipiscing in varius tortor. Mauris varius nunc enim bibendum habitasse convallis interdum. Faucibus risus mauris vestibulum quisque purus pharetra. Elit at eu diam placerat molestie blandit consectetur. Condimentum accumsan hac enim sit urna eu dolor neque aenean. Dignissim cras massa nibh purus consequat est. Morbi at nisl lacus sem.</p>
<div class="btn-fill about-btn abs">READ MORE</div>

<h2 class="gallery-title abs">Gallery</h2>

<div class="g-item abs" style="left:117px;top:1785px"><span class="g-label">Heavy Haul</span><svg class="g-arrow" width="28" height="28" viewBox="0 0 28 28"><circle cx="14" cy="14" r="13" fill="#cfe5f0" stroke="#9cc9dd"/><path d="M8 14h12M15 9l5 5-5 5" fill="none" stroke="#fff" stroke-width="2"/></svg><div class="g-photo" role="img" aria-label="Blue heavy haul lowboy trailer" style="background:linear-gradient(90deg,#2b3a8c,#1f2a6e,#3a4aa0)"></div></div>
<div class="g-item abs" style="left:461px;top:1785px"><span class="g-label">Olifield</span><svg class="g-arrow" width="28" height="28" viewBox="0 0 28 28"><circle cx="14" cy="14" r="13" fill="#cfe5f0" stroke="#9cc9dd"/><path d="M8 14h12M15 9l5 5-5 5" fill="none" stroke="#fff" stroke-width="2"/></svg><div class="g-photo" role="img" aria-label="Red oilfield trailer" style="background:linear-gradient(90deg,#d0282a,#a71d1f,#c94a3a)"></div></div>
<div class="g-item abs" style="left:806px;top:1785px"><span class="g-label">Super Haul</span><svg class="g-arrow" width="28" height="28" viewBox="0 0 28 28"><circle cx="14" cy="14" r="13" fill="#cfe5f0" stroke="#9cc9dd"/><path d="M8 14h12M15 9l5 5-5 5" fill="none" stroke="#fff" stroke-width="2"/></svg><div class="g-photo" role="img" aria-label="Black super haul multi-axle trailer" style="background:linear-gradient(90deg,#2a2a2a,#111,#3a3a3a)"></div></div>
<div class="g-item abs" style="left:117px;top:1985px"><span class="g-label">Mining</span><svg class="g-arrow" width="28" height="28" viewBox="0 0 28 28"><circle cx="14" cy="14" r="13" fill="#cfe5f0" stroke="#9cc9dd"/><path d="M8 14h12M15 9l5 5-5 5" fill="none" stroke="#fff" stroke-width="2"/></svg><div class="g-photo" role="img" aria-label="Yellow mining trailer carrying a loader" style="background:linear-gradient(90deg,#c99a10,#e2b51e,#b98a12)"></div></div>
<div class="g-item abs" style="left:461px;top:1985px"><span class="g-label">Special Purpose</span><svg class="g-arrow" width="28" height="28" viewBox="0 0 28 28"><circle cx="14" cy="14" r="13" fill="#cfe5f0" stroke="#9cc9dd"/><path d="M8 14h12M15 9l5 5-5 5" fill="none" stroke="#fff" stroke-width="2"/></svg><div class="g-photo" role="img" aria-label="Grey flatbed trailer with wooden deck" style="background:linear-gradient(90deg,#6d6d6d,#a88a63,#7a7a7a)"></div></div>
<div class="g-item abs" style="left:806px;top:1985px"><span class="g-label">OEM</span><svg class="g-arrow" width="28" height="28" viewBox="0 0 28 28"><circle cx="14" cy="14" r="13" fill="#cfe5f0" stroke="#9cc9dd"/><path d="M8 14h12M15 9l5 5-5 5" fill="none" stroke="#fff" stroke-width="2"/></svg><div class="g-photo" role="img" aria-label="Blue OEM flatbed trailer" style="background:linear-gradient(90deg,#1f3aa0,#2748c0,#1a2f86)"></div></div>

<div class="btn-fill see-all abs">SEE ALL</div>

<section class="stats abs">
  <div class="stat abs" style="left:65px;top:70px"><b>5000+</b><span>Happy Customers</span></div>
  <div class="stat abs" style="left:324px;top:70px"><b>1000</b><span>Fuel &amp; LP Trucks</span></div>
  <div class="stat abs" style="left:601px;top:70px"><b>60</b><span>Rally Stop Food Stores</span></div>
  <div class="stat abs" style="left:880px;top:70px"><b>10+</b><span>Years Experinces</span></div>
</section>

<section class="touch abs">
  <h2>Get In Touch</h2>
  <div class="btn-outline touch-btn abs">START CONVERSATION</div>
</section>

<footer class="footer abs">
  <h4 class="f-brand abs" style="font-size:19px">Calderwood</h4>
  <p class="f-about abs">Lorem ipsum dolor sit amet consectetur. Sed aenean mauris volutpat in sollicitudin maecenas libero. Urna id lacus nec faucibus.</p>
  <h4 class="f-news abs">Newsletter</h4>
  <div class="f-input abs">Enter Your Emails</div>
  <div class="f-go abs">GO</div>
  <div class="f-col abs" style="left:579px"><h4>Quick Links</h4><ul><li>Home</li><li>About</li><li>Gallery</li></ul></div>
  <div class="f-col abs" style="left:758px"><h4>Contact Us</h4><ul><li>512.555.0184</li><li>hello@calderwoodhaul.com</li></ul></div>
  <div class="f-col abs" style="left:993px"><h4>Follow Us</h4><div class="socials"><span></span><span></span><span></span></div></div>
  <p class="copyright abs">© 2023 Haul Zenith Industries All Rights Reserved.</p>
</footer>

</body>
</html>
```